Etiketten-Design für Weinflaschen gesucht
Zielgruppe
Wir sind ein Weingut und suchen für unsere Weinflaschen ein neues Etikettdesign.
Aufgabenstellung
Im Anhang sieht man unsere leeren Weinflaschen mit den neuen Kapseln. Dazu passend suchen wir die Etiketten.
Grundfarbe des Etikettes ist Weiß, Größe ca. 11cm hoch & 9cm breit!
Jede Sorte hat ihrer eigene Farbe - diese ist am Kapsel sichtbar und soll sich auch leicht im Etikett
wieder finden.
Etiketten vom Grunddesign gleich + jedoch nur an STELLEN ANDERS EINGEFÄRBT.
Am Etikett zu finden sollte sein:
- Unser Logo mit Namen (Weingut muss nicht vorhanden sein am Etikett)
- Kirchenlogo
- Sorte von Wein:
(Grüner Veltliner - Grün
Traminer - Blau
Rheinriesling - Orange
Blaufränkisch - Rot
St.Lauerent -Gelb
Zweigelt - Weiß)

```html
<!DOCTYPE html>
<html lang="de">
<head>
<meta charset="utf-8">
<title>Hallberg – Rheinriesling Etikett</title>
<link rel="stylesheet" href="https://fonts.googleapis.com/css2?family=Josefin+Sans:wght@300;400&display=swap">
<style>
  :root {
    --stage: #2b2219;
    --label-paper: #f1efed;
    --ink: #2a2a2a;
    --bracket: #555555;
    --variety-orange: #c9562f;
    --variety-orange-light: #e08a5e;
    --pattern-dark: #3a3a3a;
  }
  * { margin: 0; padding: 0; box-sizing: border-box; }
  html, body {
    width: 1200px;
    height: 962px;
    overflow: hidden;
    background: var(--stage);
  }
  .canvas {
    position: relative;
    width: 1200px;
    height: 962px;
    display: flex;
    align-items: center;
    justify-content: center;
  }
  .wine-label {
    position: relative;
    width: 665px;
    height: 820px;
    background: var(--label-paper);
    font-family: "Josefin Sans", sans-serif;
    color: var(--ink);
  }
  .corner-brackets {
    position: absolute;
    inset: 0;
    width: 100%;
    height: 100%;
  }
  .brand {
    position: absolute;
    top: 100px;
    left: 0;
    right: 0;
    display: flex;
    flex-direction: column;
    align-items: center;
  }
  .brand-mark {
    width: 72px;
    height: 72px;
    border-radius: 50%;
    background: var(--ink);
  }
  .brand-name {
    margin-top: 46px;
    font-weight: 300;
    font-size: 64px;
    letter-spacing: 4px;
    line-height: 1;
  }
  .brand-sub {
    margin-top: 18px;
    font-weight: 300;
    font-size: 13px;
    letter-spacing: 9px;
  }
  .variety {
    position: absolute;
    top: 372px;
    left: 0;
    right: 0;
    text-align: center;
    font-weight: 300;
    font-size: 42px;
    letter-spacing: 3px;
  }
  .pattern-field {
    position: absolute;
    top: 448px;
    left: 106px;
    width: 442px;
    height: 296px;
    background: linear-gradient(135deg, var(--variety-orange-light) 0%, var(--variety-orange) 45%, var(--pattern-dark) 100%);
  }
</style>
</head>
<body>
<main class="canvas">
  <article class="wine-label">
    <svg class="corner-brackets" viewBox="0 0 665 820" aria-hidden="true">
      <g fill="none" stroke="var(--bracket)" stroke-width="3">
        <polyline points="28,66 28,30 64,30"/>
        <polyline points="601,30 637,30 637,66"/>
        <polyline points="28,754 28,790 64,790"/>
        <polyline points="601,790 637,790 637,754"/>
      </g>
    </svg>
    <header class="brand">
      <span class="brand-mark" aria-hidden="true"></span>
      <span class="brand-name">Hallberg</span>
      <span class="brand-sub">WEINGUT</span>
    </header>
    <h1 class="variety">RHEINRIESLING</h1>
    <div class="pattern-field" role="img" aria-label="Geometrisches Muster aus Dreiecken und W-Formen in Orange, Rot, Grau und Schwarz"></div>
  </article>
</main>
</body>
</html>
```